Card Design Project

I need a postcard design two sides of 14 cm x 10 cm,I run Bellwren Clinical Hypnosis and Psychotherapy. Hypnotherapists use a range of effective methods to guide the exploration and resolution of inner conflict. They work with each individual to identify habitual triggers and social drivers, and to find alternative solutions.Clinical hypnotherapy is a natural and powerful way to improve health and wellbeing by overcoming personal barriers, addictions and negative behavioural patterns. Conveniently co-located with Dunmore Osteopathy Clinic in Kestrel Rd, Footscray Melbourne, Bellwren Clinical Hypnotherapy focuses on helping you to achieve your goals:
Lose weight
Quit smoking
Reduce alcohol
Overcome phobias
Alleviate anxiety
Alleviate depression
Gain confidence
I'd like a design that uses a photo of the sea 'the colors of white and blue and a photo as well .

Target Market(s)

Young professionals,educated ,caucasians, more women than men

Industry/Entity Type

Hypnotherapy

Requirements
Must have
• Logo provided , photos of sea, blue and white ,association address:
418 kestrel Rd ,Footscray Phone: 96427083 & 0427961502

WEB SITE:bellwrenclinicalhypnotherapy.com.au
location map and the mention of free car park.

```html
<!DOCTYPE html>
<html lang="en">
<head>
<meta charset="utf-8">
<title>Bellwren Hypnotherapy – Postcard</title>
<link rel="stylesheet" href="https://fonts.googleapis.com/css2?family=Questrial&family=Arimo:ital,wght@0,700;1,700&family=Mulish:ital,wght@1,400;1,800&display=swap">
<style>
  :root {
    --paper: #ffffff;
    --brand-blue: #1f5fae;
    --ink-grey: #3a3a3a;
    --frame-blue: #2a6db3;
    --sky-top: #1d67b8;
    --sky-mid: #6fa6d8;
    --sky-light: #e9f1f8;
    --sea-top: #1c6fa0;
    --sea-mid: #2c8fbd;
    --sea-bottom: #5cc3e0;
    --heading-blue: #8fc3ea;
    --map-base: #e8e6e1;
    --map-shade: #d9d6cf;
    --pin-red: #d9534f;
    --white: #ffffff;
  }
  * { margin: 0; padding: 0; box-sizing: border-box; }
  html, body { width: 857px; height: 1200px; overflow: hidden; background: var(--paper); }
  .postcard { position: relative; width: 857px; height: 1200px; background: var(--paper); }

  .brand { position: absolute; left: 60px; top: 40px; width: 730px; height: 110px; }
  .brand-mark { position: absolute; left: 20px; top: 12px; width: 90px; height: 90px; border-radius: 50%; background: var(--brand-blue); }
  .brand-name { position: absolute; left: 208px; top: 8px; font-family: "Questrial", sans-serif; font-weight: 400; font-size: 48px; color: var(--brand-blue); white-space: nowrap; }
  .brand-rule { position: absolute; left: 208px; top: 73px; width: 512px; height: 2px; background: var(--brand-blue); }
  .brand-web { position: absolute; left: 210px; top: 78px; font-family: "Questrial", sans-serif; font-size: 19px; letter-spacing: 1.6px; color: var(--ink-grey); white-space: nowrap; }

  .panel { position: absolute; left: 18px; top: 180px; width: 821px; height: 1001px; border: 3px solid var(--frame-blue); overflow: hidden; }
  .sky { position: absolute; left: 0; top: 0; width: 100%; height: 503px;
    background: linear-gradient(160deg, var(--sky-top) 0%, var(--sky-mid) 45%, var(--sky-light) 75%, var(--sky-mid) 100%); }
  .sea { position: absolute; left: 0; top: 503px; width: 100%; height: 498px;
    background: linear-gradient(180deg, var(--sea-top) 0%, var(--sea-mid) 55%, var(--sea-bottom) 100%); }

  .portrait { position: absolute; left: 34px; top: 60px; width: 308px; height: 398px; border: 5px solid var(--white);
    background: linear-gradient(180deg, #f2f2f2 0%, #dfe3e8 100%); box-shadow: 0 2px 6px rgba(0,0,0,.35); }
  .therapist { position: absolute; left: 34px; top: 460px; width: 308px; text-align: center;
    font-family: "Arimo", sans-serif; font-style: normal; font-weight: 700; font-size: 28px; letter-spacing: 1px; color: var(--ink-grey);
    text-shadow: 0 0 6px var(--white), 0 0 3px var(--white); }

  .goals-title { position: absolute; left: 382px; top: 20px; font-family: "Arimo", sans-serif; font-style: italic; font-weight: 700;
    font-size: 40px; color: var(--heading-blue); text-shadow: 2px 2px 3px rgba(0,0,0,.35); white-space: nowrap; }
  .goals { position: absolute; left: 430px; top: 74px; list-style: none; font-family: "Arimo", sans-serif; font-style: italic;
    font-weight: 700; font-size: 32px; line-height: 47px; color: var(--ink-grey); white-space: nowrap;
    text-shadow: 0 0 8px var(--white), 0 0 4px var(--white); }

  .map { position: absolute; left: 34px; top: 535px; width: 308px; height: 402px; border: 5px solid var(--white);
    background: linear-gradient(135deg, var(--map-base) 0%, var(--map-shade) 100%); box-shadow: 0 2px 6px rgba(0,0,0,.35); }
  .map-pin { position: absolute; left: 131px; top: 118px; width: 36px; height: 50px; }

  .contact { position: absolute; left: 380px; width: 420px; text-align: center; font-family: "Mulish", sans-serif; font-style: italic; color: var(--white); text-shadow: 1px 1px 3px rgba(0,0,0,.4); }
  .address { top: 586px; font-size: 35px; line-height: 44px; }
  .phones { top: 722px; font-size: 28px; line-height: 42px; }
  .parking { top: 836px; font-weight: 800; font-size: 50px; text-shadow: 2px 3px 4px rgba(0,0,0,.45); }
</style>
</head>
<body>
<main class="postcard">
  <header class="brand">
    <span class="brand-mark"></span>
    <h1 class="brand-name">Bellwren Hypnotherapy</h1>
    <span class="brand-rule"></span>
    <p class="brand-web">www.bellwrenclinicalhypnotherapy.com.au</p>
  </header>

  <section class="panel">
    <div class="sky" role="img" aria-label="Blue sky with white clouds"></div>
    <div class="sea" role="img" aria-label="Calm blue sea surface"></div>

    <div class="portrait" role="img" aria-label="Portrait photo of the hypnotherapist"></div>
    <p class="therapist">Marco Ellery</p>

    <h2 class="goals-title">Achieve your goals</h2>
    <ul class="goals">
      <li>Lose Weight</li>
      <li>Quit Smoking</li>
      <li>Reduce alcohol</li>
      <li>consumption</li>
      <li>Overcome your phobias</li>
      <li>Alleviate anxiety</li>
      <li>Alleviate depression</li>
      <li>Gain Confidence</li>
    </ul>

    <div class="map" role="img" aria-label="Street map showing the clinic location on Kestrel Rd, Footscray">
      <svg class="map-pin" viewBox="0 0 36 50" aria-hidden="true">
        <path d="M18 1C8.6 1 1 8.6 1 18c0 12.5 17 31 17 31s17-18.5 17-31C35 8.6 27.4 1 18 1z" fill="var(--pin-red)" stroke="#9e2f2b" stroke-width="1.5"/>
        <circle cx="18" cy="18" r="6" fill="var(--white)"/>
      </svg>
    </div>

    <p class="contact address">418 Kestrel Rd,<br>Footscray</p>
    <p class="contact phones">Ph: 9642 7083<br>Mobile: 04 2796 1502</p>
    <p class="contact parking">Free parking</p>
  </section>
</main>
</body>
</html>
```